Company Employee Onboarding Presentation

We need a custom PowerPoint design for a company presentation. This presentation will be sent to new employees during their onboarding/hiring process. We have attached a current mock-up of the presentation - but this is for content only. We do not like the style of the mock-up. We're a commercial real estate investment company based in Los Angeles, CA. Our website is: www.marnwickhold.com.

One artistic element that we want in the presentation is that we want a timeline similar to the attached file, but want to overlay a rising bar chart from left to right that shows the total number of units owned rising through the years. We would like this to be in the background though by using a low opacity value for the color of the graph. A great example of what we want the timeline to look like is at the bottom of the following webpage (we would just need to add the rising bar chart in the background). https://www.tolvercastlecap.com/firm. This timeline is what would take the place of page 4 of the attached PP presentation.

In addition to our company landing page, the following website is representative of a style we like: https://www.qeo.com

```html
<!DOCTYPE html>
<html lang="en">
<head>
<meta charset="utf-8">
<title>The Marnwick Group – Onboarding Slides</title>
<link rel="stylesheet" href="https://fonts.googleapis.com/css2?family=Poppins:wght@400;500;600&family=Archivo+Black&display=swap">
<style>
  :root {
    --backdrop: #7f7f7f;
    --paper: #ffffff;
    --brand-red: #e31515;
    --deep-red: #c41f26;
    --ink: #1d1d1d;
    --photo-light: #cfcfcf;
    --photo-dark: #3a3a3a;
  }
  * { margin: 0; padding: 0; box-sizing: border-box; }
  html, body { width: 1200px; height: 759px; overflow: hidden; }
  body {
    position: relative;
    background: var(--backdrop);
    font-family: "Poppins", sans-serif;
    color: var(--ink);
  }
  .slide {
    position: absolute;
    width: 506px;
    height: 284px;
    background: var(--paper);
    box-shadow: 6px 8px 14px rgba(0,0,0,0.35);
    overflow: hidden;
  }
  .slide svg.shapes { position: absolute; inset: 0; }

  /* Cover slide */
  .cover { left: 75px; top: 66px; }
  .cover .brand {
    position: absolute; left: 26px; top: 86px;
    display: flex; align-items: center; gap: 6px;
    font-size: 24px; font-weight: 500; letter-spacing: -0.3px; color: var(--ink);
  }
  .cover .brand-mark { width: 12px; height: 12px; background: var(--deep-red); }
  .cover .tagline {
    position: absolute; left: 27px; top: 114px;
    font-size: 5.6px; font-weight: 500; letter-spacing: 0.9px; text-transform: uppercase;
  }
  .cover .socials { position: absolute; left: 27px; top: 244px; display: flex; gap: 7px; }
  .cover .social-dot {
    width: 18px; height: 18px; border-radius: 50%;
    border: 1px solid var(--brand-red); background: var(--paper);
  }

  /* Values slide */
  .values { left: 620px; top: 67px; }
  .values .beliefs {
    position: absolute; left: 0; top: 0; width: 246px; height: 284px;
    background: var(--brand-red); color: var(--paper);
    padding: 12px 14px 0 11px; text-transform: uppercase;
  }
  .beliefs .belief-title { font-size: 6.3px; letter-spacing: 0.7px; line-height: 1.1; margin-bottom: 8px; }
  .beliefs .belief-text { font-size: 7.6px; font-weight: 500; letter-spacing: 0.9px; line-height: 0.98; margin-bottom: 8px; }
  .values .about { position: absolute; left: 260px; top: 0; width: 236px; height: 284px; text-transform: uppercase; }
  .about h2 {
    position: absolute; left: 0; right: 0; top: 88px; text-align: center;
    font-size: 19px; font-weight: 500; letter-spacing: 2.4px;
  }
  .about .about-text {
    position: absolute; left: 0; top: 121px; width: 236px;
    font-size: 5.9px; letter-spacing: 0.5px; line-height: 1.15; text-align: justify; text-align-last: center;
  }
  .about .about-closing {
    position: absolute; left: 2px; top: 188px; width: 234px;
    font-size: 6.8px; letter-spacing: 0.7px; line-height: 1;
  }
  .values .page-number {
    position: absolute; left: 460px; top: 231px; width: 36px; height: 36px;
    border-radius: 50%; border: 4px solid var(--brand-red); background: var(--paper);
    box-shadow: -3px 3px 6px rgba(0,0,0,0.25);
    display: flex; align-items: center; justify-content: center;
    font-size: 16px;
  }

  /* Closing slide */
  .closing { left: 346px; top: 414px; }
  .closing h2 {
    position: absolute; left: 150px; top: 95px;
    font-family: "Archivo Black", sans-serif; font-size: 30px; font-weight: 400; letter-spacing: 3px; line-height: 1;
  }
  .closing .closing-text {
    position: absolute; left: 151px; top: 134px; width: 206px;
    font-size: 4.1px; letter-spacing: 0.3px; line-height: 1.65; text-transform: uppercase;
    text-align: justify; text-align-last: center;
  }
  .closing .contact {
    position: absolute; display: flex; align-items: center; gap: 4px;
    font-size: 8.6px; font-weight: 500; letter-spacing: 1.1px; text-transform: uppercase;
  }
  .contact .icon-ring {
    width: 16px; height: 16px; border-radius: 50%; border: 1px solid var(--brand-red);
    display: flex; align-items: center; justify-content: center;
  }
  .contact-phone { left: 150px; top: 167px; }
  .contact-address { left: 258px; top: 167px; }
  .contact-social { left: 150px; top: 196px; }
</style>
</head>
<body>

<section class="slide cover">
  <svg class="shapes" viewBox="0 0 506 284" width="506" height="284" aria-hidden="true">
    <polygon points="0,0 117,0 0,79" fill="var(--deep-red)"/>
    <polygon points="298,0 506,0 506,158 369,56" fill="var(--deep-red)"/>
    <polygon points="80,284 372,58 379,62 96,284" fill="var(--brand-red)"/>
  </svg>
  <svg class="shapes" viewBox="0 0 506 284" width="506" height="284" role="img" aria-label="Black and white photograph of a row of Victorian houses behind hedges">
    <defs>
      <linearGradient id="photoTone" x1="0" y1="0" x2="0" y2="1">
        <stop offset="0" stop-color="var(--photo-light)"/>
        <stop offset="1" stop-color="var(--photo-dark)"/>
      </linearGradient>
    </defs>
    <polygon points="107,284 379,62 506,158 506,284" fill="url(#photoTone)"/>
  </svg>
  <div class="brand"><span class="brand-mark"></span>The Marnwick Group</div>
  <p class="tagline">Providing innovative housing solution worldwide</p>
  <div class="socials">
    <span class="social-dot"></span><span class="social-dot"></span><span class="social-dot"></span>
  </div>
</section>

<section class="slide values">
  <div class="beliefs">
    <p class="belief-title">We believe in being action oriented</p>
    <p class="belief-text">Results are achieved by compressing the distance between good ideas and great execution.</p>
    <p class="belief-title">We believe in authenticity</p>
    <p class="belief-text">It doesn’t take a suit and tie to solve big problems. Work hard and be yourself.</p>
    <p class="belief-title">We believe in big goals</p>
    <p class="belief-text">In order to achieve uncommon results, our goals must push us out of our comfort zone, beyond what we think is possible.</p>
    <p class="belief-title">We believe we can do well while doing good</p>
    <p class="belief-text">We give back to our communities and aim to have a lasting social impact.</p>
    <p class="belief-title">We believe work and fun are not mutually exclusive</p>
    <p class="belief-text">When done right, hard work can be a lot of fun</p>
    <p class="belief-title">We believe in a thoughtful approach.</p>
    <p class="belief-text">We utilize our experience and a considered approach to make swift, reasoned and forward-thinking decisions.</p>
  </div>
  <div class="about">
    <h2>Who we are?</h2>
    <p class="about-text">The Marnwick Group develops and invests nationally in quality real estate projects across multiple business lines. We approach business through an entrepreneurial lens, cultivating a team who acts entrepreneurially and rewards team members commensurate with their contributions. This approach drives us to produce outsized returns.</p>
    <p class="about-closing">While what we do determines our day-to-day, it’s what we believe that makes us the Marnwick Group.</p>
  </div>
  <div class="page-number">1</div>
</section>

<section class="slide closing">
  <svg class="shapes" viewBox="0 0 508 284" width="506" height="284" aria-hidden="true">
    <polygon points="0,0 138,0 0,110" fill="var(--brand-red)"/>
    <polygon points="508,175 508,284 370,284" fill="var(--brand-red)"/>
  </svg>
  <h2>THANK YOU</h2>
  <p class="closing-text">Lorem ipsum dolor sit amet, consectetur adipiscing elit, sed do eiusmod tempor incididunt ut labore et dolore magna aliqua. Quis ipsum suspendisse ultrices gravida. Risus commodo viverra maecenas accumsan lacus vel facilisis.</p>
  <div class="contact contact-phone">
    <span class="icon-ring">
      <svg width="10" height="10" viewBox="0 0 24 24" aria-hidden="true"><path fill="var(--ink)" d="M6.6 10.8a15.1 15.1 0 0 0 6.6 6.6l2.2-2.2a1 1 0 0 1 1-.25 11.4 11.4 0 0 0 3.6.57 1 1 0 0 1 1 1V20a1 1 0 0 1-1 1A17 17 0 0 1 3 4a1 1 0 0 1 1-1h3.5a1 1 0 0 1 1 1c0 1.25.2 2.45.57 3.57a1 1 0 0 1-.25 1z"/></svg>
    </span>5550142873
  </div>
  <div class="contact contact-address">
    <span class="icon-ring">
      <svg width="10" height="10" viewBox="0 0 24 24" aria-hidden="true"><path fill="var(--ink)" d="M12 2a7 7 0 0 0-7 7c0 5.2 7 13 7 13s7-7.8 7-13a7 7 0 0 0-7-7zm0 9.5A2.5 2.5 0 1 1 12 6.5a2.5 2.5 0 0 1 0 5z"/></svg>
    </span>My address
  </div>
  <div class="contact contact-social">
    <span class="icon-ring"></span>Lorem ipsum
  </div>
</section>

</body>
</html>
```